Standardization and redesign of graphics for a non-fiction book

For a book project, 11 graphics need to be visually unified so that all the graphics in the book are in the same style. The graphics must be created from scratch. Just new colors aren't enough. Some of the existing graphics are by other authors who own the copyright. Accordingly, the new graphics must be truly new. This is especially true for the "2 S-curves" graphic.

Target Market(s)

Manager Furniture Industry

Industry/Entity Type

Möbel

Colors
0054AA
0677BA
7BADD7
CADEEF
E8F1F8

```html
<!DOCTYPE html>
<html lang="de">
<head>
<meta charset="utf-8">
<title>Entwicklung des deutschen Möbelhandels 2014 – 2024</title>
<link href="https://fonts.googleapis.com/css2?family=Poppins:ital,wght@0,400;0,700;1,400&display=swap" rel="stylesheet">
<style>
  :root {
    --brand-blue: #0054AA;
    --mid-blue: #0677BA;
    --light-blue: #7BADD7;
    --area-grey: #E6E6E6;
    --grid-grey: #9A9A9A;
    --label-grey: #6E6E6E;
    --band-start: #0FA5D6;
    --band-end: #2AFFF6;
    --line-start: #4AA3E4;
    --line-end: #0A3FA8;
    --canvas: #FFFFFF;
  }
  html, body {
    margin: 0;
    padding: 0;
    width: 1200px;
    height: 1200px;
    overflow: hidden;
    background: var(--canvas);
  }
  .chart {
    display: block;
    width: 1200px;
    height: 1200px;
    font-family: "Poppins", sans-serif;
  }
  .chart-title { fill: var(--brand-blue); font-weight: 700; font-size: 34px; }
  .chart-subtitle { fill: var(--brand-blue); font-style: italic; font-size: 28px; }
  .axis-label { fill: var(--label-grey); font-size: 18px; }
  .gridline { stroke: var(--grid-grey); stroke-width: 1; }
  .area-total { fill: var(--area-grey); }
  .trend-line { fill: none; stroke: url(#lineGradient); stroke-width: 9; stroke-linejoin: round; }
</style>
</head>
<body>
<svg class="chart" viewBox="0 0 1500 1500" xmlns="http://www.w3.org/2000/svg" role="img" aria-label="Diagramm zur Entwicklung des deutschen Möbelhandels 2014 bis 2024">
  <defs>
    <linearGradient id="bandGradient" x1="262" y1="0" x2="1222" y2="0" gradientUnits="userSpaceOnUse">
      <stop offset="0" stop-color="var(--band-start)"/>
      <stop offset="1" stop-color="var(--band-end)"/>
    </linearGradient>
    <linearGradient id="lineGradient" x1="258" y1="0" x2="1230" y2="0" gradientUnits="userSpaceOnUse">
      <stop offset="0" stop-color="var(--line-start)"/>
      <stop offset="1" stop-color="var(--line-end)"/>
    </linearGradient>
  </defs>

  <text class="chart-title" x="742" y="485" text-anchor="middle">Entwicklung des deutschen Möbelhandels 2014 – 2024</text>
  <text class="chart-subtitle" x="730" y="523" text-anchor="middle">in Mrd CHF</text>

  <g class="gridlines">
    <line class="gridline" x1="205" y1="580" x2="262" y2="580"/>
    <line class="gridline" x1="205" y1="650" x2="262" y2="650"/>
    <line class="gridline" x1="205" y1="720" x2="262" y2="720"/>
    <line class="gridline" x1="205" y1="790" x2="262" y2="790"/>
    <line class="gridline" x1="205" y1="860" x2="262" y2="860"/>
    <line class="gridline" x1="205" y1="930" x2="1285" y2="930"/>
    <line class="gridline" x1="1222" y1="580" x2="1285" y2="580"/>
    <line class="gridline" x1="1222" y1="650" x2="1285" y2="650"/>
    <line class="gridline" x1="1222" y1="720" x2="1285" y2="720"/>
    <line class="gridline" x1="1222" y1="790" x2="1285" y2="790"/>
    <line class="gridline" x1="1222" y1="860" x2="1285" y2="860"/>
  </g>

  <polygon class="area-total" points="262,552 358,573 455,578 568,591 740,601 845,608 935,610 1020,619 1130,628 1222,637 1224,930 262,930"/>
  <polygon class="area-band" fill="url(#bandGradient)" points="262,540 360,550 455,550 568,560 740,564 845,541 1010,540 1130,552 1222,562 1222,637 1130,628 1020,619 935,610 845,608 740,601 568,591 455,578 358,573 262,552"/>

  <polyline class="trend-line" points="258,852 752,760 845,658 945,623 1040,623 1130,610 1230,602"/>

  <g class="axis-label axis-left" text-anchor="end">
    <text x="194" y="576">5.000</text>
    <text x="194" y="667">4.000</text>
    <text x="194" y="721">3.000</text>
    <text x="194" y="791">2.000</text>
    <text x="194" y="861">1.000</text>
    <text x="194" y="931">0.000</text>
  </g>

  <g class="axis-label axis-right">
    <text x="1306" y="576">20.0%</text>
    <text x="1306" y="608">18.0%</text>
    <text x="1306" y="657">16.0%</text>
    <text x="1306" y="695">14.0%</text>
    <text x="1306" y="729">12.0%</text>
    <text x="1306" y="764">10.0%</text>
    <text x="1306" y="798">8.0%</text>
    <text x="1306" y="832">6.0%</text>
    <text x="1306" y="864">4.0%</text>
    <text x="1306" y="897">2.0%</text>
    <text x="1306" y="931">0.0%</text>
  </g>

  <g class="axis-label axis-years" text-anchor="middle">
    <text x="266" y="981">2014</text>
    <text x="313" y="981">|</text>
    <text x="361" y="981">2015</text>
    <text x="407" y="981">|</text>
    <text x="455" y="981">2016</text>
    <text x="501" y="981">|</text>
    <text x="548" y="981">2017</text>
    <text x="595" y="981">|</text>
    <text x="641" y="981">2018</text>
    <text x="689" y="981">|</text>
    <text x="736" y="981">2019</text>
    <text x="783" y="981">|</text>
    <text x="832" y="981">2020</text>
    <text x="882" y="981">|</text>
    <text x="929" y="981">2021</text>
    <text x="975" y="981">|</text>
    <text x="1024" y="981">2022</text>
    <text x="1073" y="981">|</text>
    <text x="1122" y="981">2023</text>
    <text x="1171" y="981">|</text>
    <text x="1221" y="981">2024</text>
  </g>
</svg>
</body>
</html>
```